Digital Billboard Design: Winter Sales Event

I own a boutique furniture store in Calgary, AB (maplewoven.ca) and I am looking to advertise our winter sale event on a new curved digital billboard (specs attached including required file type).

I have this billboard rented for 52-weeks so I will be looking to change the design every 4-weeks (i.e. this is intended to be an ongoing project).

The objective of this first billboard is to raise awareness around our annual winter sales event. The store itself is only a few blocks from the billboard so those commuting into downtown are just a short drive from the store.

I am looking for a fresh, clean, contemporary look that will grab your attention as you drive into downtown Calgary without presenting to much info so as to be distracting (and overwhelming -- the billboard does not need to contain all info on my current marketing material). I should also note that the store caters to a higher-end, more sophisticated clientele so the graphics need to reflect the brand (i.e. we are not Brenton Furniture or Couch Depot!).

I have attached three files:

Billboard specs
Current marketing material advertising sale (and all relevant data)
An idea that is from an American furniture store that I think is interesting

Target Market(s)

Upper middle class, sophisticated client who appreciates the finer things in life.

Industry/Entity Type

Furniture Store

Font styles to use
Sans Serif

Requirements
Must have
• Company Logo
• Winter Sales Event - 20 to 60% off
• Address: 3847 22nd Ave SW
Nice to have
• Image of furniture -- see our website www.maplewoven.ca -- any photo from this site can be used
Should not have
• Too much text or visual distration

```html
<!DOCTYPE html>
<html lang="en">
<head>
<meta charset="utf-8">
<title>Winter Sales Event Billboard</title>
<link href="https://fonts.googleapis.com/css2?family=Montserrat:wght@300;400;500;600;700&display=swap" rel="stylesheet">
<style>
  :root {
    --page-bg: #ffffff;
    --board-top: #3d4651;
    --board-bottom: #262c34;
    --text-main: #ffffff;
    --text-muted: #9aa1aa;
    --rule: #7d848d;
    --photo-light: #e6dfcf;
    --photo-mid: #c9bea6;
    --photo-dark: #5a5246;
  }
  * { margin: 0; padding: 0; box-sizing: border-box; }
  html, body {
    width: 1145px;
    height: 1200px;
    overflow: hidden;
    background: var(--page-bg);
  }
  .billboard {
    position: absolute;
    left: 40px;
    top: 376px;
    width: 1065px;
    height: 448px;
    background: radial-gradient(ellipse at 70% 35%, var(--board-top) 0%, var(--board-bottom) 85%);
    font-family: "Montserrat", sans-serif;
    color: var(--text-main);
    overflow: hidden;
  }
  .headline {
    position: absolute;
    left: 26px;
    top: 27px;
    font-size: 80px;
    font-weight: 300;
    line-height: 1;
    letter-spacing: 3px;
    white-space: nowrap;
  }
  .headline strong { font-weight: 700; }
  .offer {
    position: absolute;
    left: 26px;
    top: 130px;
    font-size: 82px;
    font-weight: 700;
    line-height: 1;
    white-space: nowrap;
  }
  .offer .joiner {
    font-weight: 400;
    font-size: 56px;
    margin: 0 14px;
  }
  .divider {
    position: absolute;
    left: 28px;
    top: 228px;
    width: 600px;
    height: 2px;
    background: var(--rule);
  }
  .store-name {
    position: absolute;
    left: 28px;
    top: 266px;
    font-size: 44px;
    font-weight: 300;
    line-height: 1;
    letter-spacing: 10px;
    color: var(--text-main);
    white-space: nowrap;
  }
  .store-name .second { color: var(--text-muted); }
  .address {
    position: absolute;
    left: 28px;
    top: 328px;
    font-size: 47px;
    font-weight: 500;
    line-height: 55px;
    white-space: nowrap;
  }
  .product-photo {
    position: absolute;
    left: 650px;
    top: 244px;
    width: 385px;
    height: 196px;
    border-radius: 10px;
    background: linear-gradient(170deg, var(--photo-light) 0%, var(--photo-mid) 60%, var(--photo-dark) 100%);
    opacity: 0.92;
  }
</style>
</head>
<body>
  <section class="billboard">
    <h1 class="headline">WINTER <strong>SALES</strong> EVENT</h1>
    <p class="offer">SAVE 20<span class="joiner">TO</span>60%</p>
    <div class="divider"></div>
    <p class="store-name">MAPLE <span class="second">WOVEN</span></p>
    <p class="address">3847 22ND AVE SW,<br>CALGARY, AB</p>
    <div class="product-photo" role="img" aria-label="Photo of a cream upholstered bed with curved headboard and footboard, white linens and pillows"></div>
  </section>
</body>
</html>
```